Trendy eye catching business card for lawn mowing business

Verge Crew, a local community lawn mowing service, requires an eye catching trendy business card to drop into letterboxes.

We could simply throw something together from a Microsoft Word template, but we are wanting something more than this. Some other business’ images are attached for some inspiration.

We are requiring the card to have Verge Crew with our slogan, Call The Pellows. In addition, provide details with that we are a local, affordable lawn mowing service, and for other gardening matters to simply just ask!
Plus the relevant contact details, phone, email, social media.

Target Market(s)

Local community members who require assistance with their garden care

Industry/Entity Type

Gardening

Contact Information for Business Card

the name VERGE CREW is our logo
telephone logo 0493 218 067
email logo vergecrew@postbox-example.com
Instagram logo vergecrew
Facebook logo vergecrew.sth
Lawn Mowing Service
Local Affordable
edge trim, blow and clipping removal included.
Other gardening matters, just ask!

Font styles to use
Serif
Sans Serif
Decorative
Script

Colors
9bcb3c
ffffff

Requirements
Must have
• All the details listed in Business Card Details.
Make these words prominent:
Verge Crew
Lawn Mowing Service
Local
Affordable
Nice to have
• Our slogan ‘Call The Pellows’ incorporated.
Different colour background for front and reverse side
Greens, white and black colours
Subtle grass blades images incorporated
Should not have
• No images of lawnmowers.
No images of men/cartoons.
No using initials for Verge Crew

```html
<!DOCTYPE html>
<html lang="en">
<head>
<meta charset="utf-8">
<title>Verge Crew – Business Cards</title>
<link rel="stylesheet" href="https://fonts.googleapis.com/css2?family=Oswald:wght@600&family=Poppins:wght@300;400;600;700&family=Kaushan+Script&display=swap">
<style>
  :root {
    --green: #9bcb3c;
    --green-deep: #7fb02a;
    --charcoal: #2d2d2d;
    --ink: #262626;
    --paper: #ffffff;
    --backdrop: #e4e4e4;
    --rule-dark: #555555;
  }
  * { box-sizing: border-box; margin: 0; padding: 0; }
  html, body { width: 1200px; height: 566px; overflow: hidden; }
  body {
    background: var(--backdrop);
    display: flex;
    align-items: center;
    justify-content: center;
    gap: 32px;
    font-family: "Poppins", sans-serif;
  }
  .card {
    position: relative;
    width: 560px;
    height: 320px;
    overflow: hidden;
    box-shadow: 0 6px 18px rgba(0,0,0,.18);
  }
  .card--back { background: var(--charcoal); color: var(--paper); }
  .card--front { background: var(--paper); color: var(--ink); }

  .brand {
    position: absolute;
    left: 52px;
    top: 52px;
    width: 178px;
    text-align: center;
  }
  .brand__name {
    font-family: "Oswald", sans-serif;
    font-weight: 600;
    font-size: 62px;
    line-height: .98;
    letter-spacing: 1px;
    text-transform: uppercase;
    color: var(--green);
  }
  .card--front .brand__name { color: var(--charcoal); }
  .brand__slogan {
    margin-top: 14px;
    font-family: "Kaushan Script", cursive;
    font-size: 19px;
    color: var(--paper);
  }
  .card--front .brand__slogan { color: var(--ink); }
  .brand__slogan em { font-style: normal; color: var(--green); }

  .divider {
    position: absolute;
    left: 270px;
    top: 66px;
    width: 1px;
    height: 165px;
    background: var(--rule-dark);
  }

  .contacts {
    position: absolute;
    left: 305px;
    top: 92px;
    list-style: none;
    font-size: 12.5px;
    font-weight: 300;
    line-height: 21px;
  }
  .contacts li { display: flex; align-items: center; gap: 10px; }
  .contacts li.gap { margin-top: 21px; }
  .contacts svg { width: 13px; height: 13px; flex: none; }

  .tagline {
    position: absolute;
    font-family: "Kaushan Script", cursive;
    font-size: 13px;
  }
  .tagline em { font-style: normal; color: var(--green); }
  .card--back .tagline { left: 305px; top: 212px; }
  .card--front .tagline { left: 290px; top: 210px; }

  .offer { position: absolute; left: 290px; top: 68px; }
  .offer__local {
    display: inline-block;
    font-size: 17px;
    font-weight: 300;
    letter-spacing: .3px;
    padding-bottom: 4px;
    border-bottom: 1px solid var(--ink);
  }
  .offer__local span { color: var(--green); margin: 0 6px; }
  .offer__title {
    margin-top: 9px;
    font-size: 23px;
    font-weight: 700;
    line-height: 1.08;
    color: var(--charcoal);
  }
  .offer__title span { color: var(--green); display: block; }
  .offer__note {
    margin-top: 8px;
    font-size: 12.5px;
    line-height: 1.3;
    font-weight: 400;
  }

  .grass {
    position: absolute;
    left: 0;
    bottom: 0;
    width: 100%;
    height: 62px;
    background: linear-gradient(to bottom, rgba(155,203,60,0) 0%, rgba(155,203,60,.55) 35%, var(--green) 70%, var(--green-deep) 100%);
  }
</style>
</head>
<body>

  <section class="card card--back">
    <div class="brand">
      <div class="brand__name">Verge<br>Crew</div>
      <p class="brand__slogan">Call the <em>Pellows</em></p>
    </div>
    <div class="divider"></div>
    <ul class="contacts">
      <li>
        <svg viewBox="0 0 16 16" fill="none" stroke="#9bcb3c" stroke-width="1.4"><path d="M3 2h3l1.5 3.5-2 1.3a8 8 0 0 0 3.7 3.7l1.3-2L14 10v3a1 1 0 0 1-1 1A11 11 0 0 1 2 3a1 1 0 0 1 1-1z"/></svg>
        0493 218 067
      </li>
      <li>
        <svg viewBox="0 0 16 16" fill="none" stroke="#9bcb3c" stroke-width="1.4"><rect x="1.5" y="3.5" width="13" height="9"/><path d="M1.5 3.5 8 9l6.5-5.5"/></svg>
        vergecrew@postbox-example.com
      </li>
      <li class="gap">
        <svg viewBox="0 0 16 16" fill="none" stroke="#9bcb3c" stroke-width="1.4"><rect x="2" y="2" width="12" height="12" rx="2"/></svg>
        /vergecrew
      </li>
      <li>
        <svg viewBox="0 0 16 16" fill="none" stroke="#9bcb3c" stroke-width="1.4"><circle cx="8" cy="8" r="6.3"/></svg>
        fb.me/vergecrew.sth
      </li>
    </ul>
    <p class="tagline">Other gardening matters, <em>just ask!</em></p>
    <div class="grass" role="img" aria-label="Band of green grass blades along the bottom edge"></div>
  </section>

  <section class="card card--front">
    <div class="brand">
      <div class="brand__name">Verge<br>Crew</div>
      <p class="brand__slogan">Call the <em>Pellows</em></p>
    </div>
    <div class="offer">
      <p class="offer__local">LOCAL<span>|</span>AFFORDABLE</p>
      <h2 class="offer__title"><span>LAWN MOWING</span>SERVICE</h2>
      <p class="offer__note">Edge trim, blow and clipping<br>removal included.</p>
    </div>
    <p class="tagline">Other gardening matters, <em>just ask!</em></p>
    <div class="grass" role="img" aria-label="Band of green grass blades along the bottom edge"></div>
  </section>

</body>
</html>
```